Brochure Lantern Ridge Advisory

need brochure to display my services. We are a business consulting firm focused on small to medium size business. We also do speaking engagements and trainings on leadership development as well as help local suppliers bring products to mark
et. I have some specific ideas regarding setup. Would like to follow color scheme of my logo and my business cards. Like the black background. Also with setup would like the following:
Cover - Logo and Mission statement
Back - Bio
Inside( fully opened brochure) array of services separated by catagory
inside flap - mission/vision/purpose
I will upload sketch of this as well as Mission/Vision/Purpose statements

Target Market(s)

small to medium size business owners
local vendors
any purveyor of services or goods

Industry/Entity Type

Business Consultant

Font styles to use
Serif

Requirements
Must have
• want to include the following:
• Logo
• contact information
• bio
• array of services
• mission/vision/purpose statement - to be added to files later today
Nice to have
• Cover: Logo, Mission statement
• Back : Bio
• Inside: array of services on 3 inside pages; broken out onto 3 categories, 1 per page.
• will upload sketch of this

```html
<!DOCTYPE html>
<html lang="en">
<head>
<meta charset="utf-8">
<title>Lantern Ridge Advisory – Trifold Brochure</title>
<link href="https://fonts.googleapis.com/css2?family=Oswald:wght@500;600&family=Open+Sans:wght@400;600;700&display=swap" rel="stylesheet">
<style>
:root{
  --ink:#151515;
  --ink-2:#222;
  --green:#7cb82f;
  --orange:#f28c1c;
  --white:#ffffff;
  --muted:#cfcfcf;
  --page:#ffffff;
}
*{box-sizing:border-box;margin:0;padding:0}
html,body{width:887px;height:1200px;overflow:hidden;background:var(--page)}
body{position:relative;font-family:"Open Sans",Arial,sans-serif;color:var(--muted)}
.spread{position:absolute;left:30px;width:828px;height:524px;display:flex;box-shadow:0 4px 14px rgba(0,0,0,.25)}
.spread--outside{top:48px}
.spread--inside{top:636px}
.panel{position:relative;width:276px;height:100%;background:var(--ink);overflow:hidden}
.photo{position:absolute;left:0;top:0;width:100%}
.wave{position:absolute;left:0;width:100%;height:70px}
.content{position:absolute;left:22px;right:22px}
.heading{font-family:"Oswald",Arial,sans-serif;font-weight:600;letter-spacing:.5px;text-transform:uppercase}
.heading--orange{color:var(--orange)}
.heading--green{color:var(--green)}
.heading--sm{font-size:13px;margin:10px 0 4px}
.body-text{font-size:7.4px;line-height:1.55;color:var(--muted)}
.body-text + .body-text{margin-top:6px}
.contact{position:absolute;left:0;bottom:0;width:100%;height:28px;background:var(--ink-2);display:flex;align-items:center;gap:16px;padding:0 22px;font-size:7.5px;color:var(--white)}
.contact span{display:flex;align-items:center;gap:5px}
.round-photo{position:absolute;border-radius:50%;border:4px solid var(--orange)}
.brand{position:absolute;left:0;width:100%;text-align:center}
.brand__mark{display:inline-block;width:12px;height:12px;border-radius:50%;background:var(--green);margin-bottom:5px}
.brand__name{font-family:"Oswald",Arial,sans-serif;font-weight:500;font-size:19px;color:var(--white);letter-spacing:1px;text-transform:uppercase;line-height:1.1}
.tagline{position:absolute;left:0;width:100%;padding:12px 20px;background:var(--orange);text-align:left}
.tagline__lead{font-family:"Oswald",Arial,sans-serif;font-weight:600;font-size:17px;color:var(--white);line-height:1.15}
.tagline__sub{font-size:7px;font-weight:700;color:var(--ink);margin-top:4px;text-transform:uppercase;line-height:1.4}
.url{position:absolute;bottom:14px;right:20px;font-size:9px;font-weight:700;color:var(--green)}
.service-list{list-style:none;font-size:8px;color:var(--white);line-height:1.75}
.service-list li::before{content:"";display:inline-block;width:4px;height:4px;background:var(--green);border-radius:50%;margin:0 6px 1px 0}
.cols{display:flex;gap:14px}
</style>
</head>
<body>

<!-- Outside: flap, back, cover -->
<section class="spread spread--outside">

  <article class="panel panel--flap">
    <div class="photo" role="img" aria-label="Photo of a smiling businesswoman working at a laptop in a bright office" style="height:250px;background:linear-gradient(135deg,#d9d2c6,#9b8f80 60%,#5f574d)"></div>
    <svg class="wave" style="top:214px" viewBox="0 0 276 70" preserveAspectRatio="none">
      <path d="M0 40 Q120 -6 276 18 L276 70 L0 70Z" fill="var(--green)"/>
      <path d="M0 52 Q130 10 276 34 L276 70 L0 70Z" fill="var(--ink)"/>
    </svg>
    <div class="content" style="top:276px">
      <h3 class="heading heading--orange heading--sm">Mission</h3>
      <p class="body-text">We help small and medium businesses grow with clarity, purpose and lasting results in every market they serve.</p>
      <h3 class="heading heading--orange heading--sm">Purpose</h3>
      <p class="body-text">To give owners the tools, guidance and support they need to build strong teams, sound plans and steady growth.</p>
      <h3 class="heading heading--orange heading--sm">Vision</h3>
      <p class="body-text">A community of thriving local businesses led by confident people who serve their customers and neighbours well.</p>
    </div>
    <div class="contact">
      <span><svg width="9" height="9" viewBox="0 0 24 24"><path fill="var(--green)" d="M6.6 10.8a15 15 0 0 0 6.6 6.6l2.2-2.2c.3-.3.7-.4 1-.2 1.1.4 2.3.6 3.6.6.6 0 1 .4 1 1V20c0 .6-.4 1-1 1A17 17 0 0 1 3 4c0-.6.4-1 1-1h3.5c.6 0 1 .4 1 1 0 1.3.2 2.5.6 3.6.1.3 0 .7-.2 1z"/></svg>(555) 014-2290</span>
      <span><svg width="10" height="8" viewBox="0 0 24 18"><rect x="1" y="1" width="22" height="16" fill="none" stroke="var(--green)" stroke-width="2"/><path d="M1 1l11 9 11-9" fill="none" stroke="var(--green)" stroke-width="2"/></svg>info@lanternridgeadvisory.com</span>
    </div>
  </article>

  <article class="panel panel--bio">
    <h2 class="heading heading--orange" style="position:absolute;top:12px;width:100%;text-align:center;font-size:15px">Trusted Expertise</h2>
    <div class="round-photo" role="img" aria-label="Portrait photo of the company founder" style="left:113px;top:36px;width:50px;height:50px;background:linear-gradient(135deg,#c9a27e,#7a5a3e)"></div>
    <div class="content" style="top:100px">
      <p class="body-text">Our founder has spent many years working beside owners of small and medium sized businesses, helping them plan wisely, lead well and turn good ideas into steady, profitable companies that last.</p>
      <p class="body-text">From first business plans to growing sales teams, the work is hands on and practical. Every client receives honest advice, clear next steps and a partner who stays with them as goals change over time.</p>
      <p class="body-text">Alongside consulting, we lead talks and training sessions on leadership development, and we help local suppliers bring their products to market through sound planning, purchasing and merchandising support.</p>
      <p class="body-text">We believe strong communities are built by strong local businesses, and we are proud to play a part in their success every day.</p>
    </div>
    <svg class="wave" style="bottom:0" viewBox="0 0 276 70" preserveAspectRatio="none">
      <path d="M0 30 Q150 70 276 20 L276 70 L0 70Z" fill="var(--orange)"/>
      <path d="M0 46 Q150 80 276 40 L276 70 L0 70Z" fill="var(--green)"/>
    </svg>
  </article>

  <article class="panel panel--cover">
    <div class="photo" role="img" aria-label="Photo of smiling bakery staff behind a counter of fresh bread" style="height:230px;background:linear-gradient(135deg,#e4c79a,#b0824e 55%,#6b4a2a)"></div>
    <svg class="wave" style="top:190px" viewBox="0 0 276 70" preserveAspectRatio="none">
      <path d="M0 22 Q140 60 276 26 L276 70 L0 70Z" fill="var(--green)"/>
      <path d="M0 36 Q140 74 276 40 L276 70 L0 70Z" fill="var(--ink)"/>
    </svg>
    <div class="brand" style="top:262px">
      <div class="brand__mark"></div>
      <div class="brand__name">Lantern Ridge<br>Advisory</div>
    </div>
    <div class="tagline" style="top:350px">
      <div class="tagline__lead">TO ENCOURAGE AND SUPPORT</div>
      <div class="tagline__sub">the growth of small to medium size business through practical, strategic guidance</div>
    </div>
    <div class="url">www.lanternridgeadvisory.com</div>
  </article>
</section>

<!-- Inside: three service categories -->
<section class="spread spread--inside">

  <article class="panel">
    <div class="photo" role="img" aria-label="Photo of three smiling bakers holding fresh bread" style="height:260px;background:linear-gradient(135deg,#efd9b5,#c08b55 55%,#7c5330)"></div>
    <svg class="wave" style="top:222px" viewBox="0 0 276 70" preserveAspectRatio="none">
      <path d="M0 30 Q140 70 276 10 L276 70 L0 70Z" fill="var(--orange)"/>
      <path d="M0 44 Q140 80 276 28 L276 70 L0 70Z" fill="var(--ink)"/>
    </svg>
    <div class="content" style="top:320px">
      <h2 class="heading heading--green" style="font-size:15px;line-height:1.15;margin-bottom:10px">Products to<br>Market</h2>
      <div class="cols">
        <ul class="service-list"><li>Product Development</li><li>Business Plans</li><li>Marketing</li><li>Logistics</li></ul>
        <ul class="service-list"><li>Purchasing</li><li>Merchandising</li><li>Resource Development</li></ul>
      </div>
    </div>
    <svg class="wave" style="bottom:0" viewBox="0 0 276 70" preserveAspectRatio="none">
      <path d="M0 48 Q140 30 276 56 L276 70 L0 70Z" fill="var(--green)"/>
    </svg>
  </article>

  <article class="panel">
    <div class="photo" role="img" aria-label="Photo of a smiling woman in a bakery apron" style="height:250px;background:linear-gradient(135deg,#dcc1a0,#a27752 55%,#5e4128)"></div>
    <svg class="wave" style="top:200px;height:80px" viewBox="0 0 276 80" preserveAspectRatio="none">
      <path d="M0 70 L276 10 L276 80 L0 80Z" fill="var(--orange)"/>
      <path d="M0 80 L276 26 L276 80Z" fill="var(--ink)"/>
    </svg>
    <div class="round-photo" role="img" aria-label="Photo of a small storefront building" style="left:106px;top:252px;width:64px;height:64px;background:linear-gradient(135deg,#9bc0dd,#c77b4a)"></div>
    <div class="content" style="top:330px">
      <h2 class="heading heading--orange" style="font-size:13px;margin-bottom:8px">Business Start Up</h2>
      <div class="cols">
        <ul class="service-list"><li>Start Ups</li><li>Business Plans</li><li>Marketing</li><li>Merchandising</li><li>Sales Growth</li></ul>
        <ul class="service-list"><li>Profitability</li><li>Training &amp; Development</li><li>Recruiting &amp; Hiring</li><li>Networking</li><li>Research &amp; Development</li></ul>
      </div>
    </div>
  </article>

  <article class="panel">
    <div class="photo" role="img" aria-label="Photo of a smiling businessman with glasses working on a laptop" style="height:280px;background:linear-gradient(135deg,#eef0f2,#b8bec4 55%,#6e757c)"></div>
    <svg class="wave" style="top:240px" viewBox="0 0 276 70" preserveAspectRatio="none">
      <path d="M0 20 Q120 64 276 26 L276 70 L0 70Z" fill="var(--green)"/>
      <path d="M0 34 Q120 78 276 42 L276 70 L0 70Z" fill="var(--ink)"/>
    </svg>
    <div class="content" style="top:320px">
      <h2 class="heading heading--orange" style="font-size:13px;margin-bottom:6px">Lectures &amp; Seminars</h2>
      <div class="cols" style="margin-bottom:8px">
        <ul class="service-list"><li>Leadership</li><li>Team Building</li></ul>
        <ul class="service-list"><li>Motivation</li><li>Leadership Development</li></ul>
      </div>
      <p class="body-text">Our talks and training sessions give owners, managers and teams practical tools to lead with confidence. Each session is shaped around your goals, whether you need a keynote for a local event, a workshop for new managers or ongoing coaching that builds strong habits across your whole team over time.</p>
    </div>
  </article>
</section>

</body>
</html>
```